Financial Markets Algorithmic Trading solution needs One pager Marketing designs

We are creating Marketing sheets that will be handed to potential clients that will give a broad base of our products available. We are an established Sell side firm in the financial Industry and our product focus is a Technology base solution and we want to showcases our Algorithmic trading suite.
Our customer base is Buy-side Traders,hedge funds, managing directors. We want a clean high end technology based look that will encompass the colors that are in our logo.
We intend to work with the designer after initial design to encompass the theme to other pages we have. So we will need a design that can be part of a set but can stand alone.

** i have uploaded a new File that is the correct File to design to. Please follow the flow of the categories and what resides under those headers. This is key for the delivery of the material****

Target Market(s)

Finance- Buy side firms, geared for meetings and info sheets to be left with clients who are CEO's , Head Traders, Managing Directors

Industry/Entity Type

Financial Service

Font styles to use
Other font styles liked:
• Tw Cen MT

Requirements
Must have
• Must include the logo, and encompass the colors that are in the logo.
• We want this to have a Technology company feel to it. We would like it clean and unique, all while not falling into the normal classic business look.
• Also for this page we would like to keep the layout similar to what we have.
• Please keep the style of lettering
Should not have
• Messy look, overpowering color. no cartoon graphics

```html
<!DOCTYPE html>
<html lang="en">
<head>
<meta charset="utf-8">
<title>Algorithmic Trading Strategy Overview</title>
<link href="https://fonts.googleapis.com/css2?family=Jost:wght@500;600;700&family=Source+Sans+3:wght@400;600&display=swap" rel="stylesheet">
<style>
  :root {
    --orange: #f07c22;
    --orange-deep: #e0661a;
    --orange-light: #f7a150;
    --blue: #0e5591;
    --blue-deep: #0a3f70;
    --blue-light: #1f71b1;
    --ink: #1b1b1b;
    --text: #2c2c2c;
    --paper: #ffffff;
    --stage: #d9d9d9;
  }
  * { box-sizing: border-box; margin: 0; padding: 0; }
  html, body { width: 1200px; height: 1013px; overflow: hidden; }
  body { background: var(--stage); font-family: "Source Sans 3", "Segoe UI", sans-serif; }

  .sheet {
    position: absolute; left: 249px; top: 15px;
    width: 701px; height: 983px;
    background: var(--paper); overflow: hidden;
    box-shadow: 0 4px 18px rgba(0,0,0,.25);
  }
  .hero { position: absolute; left: 0; top: 0; }

  .brand { position: absolute; left: 20px; top: 372px; display: flex; align-items: center; gap: 10px; }
  .brand-square { width: 16px; height: 16px; background: var(--blue); }
  .brand-name { font-family: "Jost", sans-serif; font-weight: 600; font-size: 20px; color: var(--ink); }

  .title {
    position: absolute; left: 20px; top: 435px;
    font-family: "Jost", sans-serif; font-weight: 600; font-size: 33px;
    color: var(--ink); letter-spacing: .3px;
  }
  .intro {
    position: absolute; left: 20px; top: 478px; width: 662px;
    font-size: 10.6px; line-height: 13.7px; color: var(--text); text-align: justify;
  }

  .strategies {
    position: absolute; left: 0; top: 596px; width: 701px; height: 293px;
    background: linear-gradient(180deg, var(--blue-deep), var(--blue) 30%, var(--blue-light));
  }
  .column { position: absolute; top: -17px; width: 190px; text-align: center; color: #fff; }
  .column.liquidity { left: 20px; }
  .column.schedule { left: 255px; }
  .column.dynamic { left: 492px; }

  .tab {
    width: 154px; height: 60px; margin: 0 auto 8px;
    background: linear-gradient(180deg, var(--orange-light), var(--orange) 55%, var(--orange-deep));
    box-shadow: 0 3px 4px rgba(0,0,0,.3);
    display: flex; align-items: center; justify-content: center;
    font-family: "Jost", sans-serif; font-weight: 600; font-size: 18.5px; line-height: 24px;
    color: var(--ink); letter-spacing: .4px;
  }
  .strategy-name {
    font-family: "Jost", sans-serif; font-weight: 600; font-size: 16px;
    color: var(--orange); text-decoration: underline; text-decoration-color: #fff;
    text-underline-offset: 3px; margin-bottom: 2px;
  }
  .strategy-text { font-size: 10.2px; line-height: 12.4px; text-align: justify; text-align-last: center; margin-bottom: 14px; }
  .footnote { font-size: 9.4px; text-align: left; padding-left: 2px; }

  .rule { position: absolute; left: 0; top: 889px; width: 701px; height: 4px; background: #fff; }
  .contact {
    position: absolute; left: 0; top: 893px; width: 701px; height: 90px;
    background: linear-gradient(90deg, var(--orange-deep), var(--orange) 25%, var(--orange-light) 55%, var(--orange) 80%, var(--orange-deep));
    color: var(--ink);
  }
  .contact-name {
    position: absolute; left: 0; width: 100%; top: 8px; text-align: center;
    font-family: "Jost", sans-serif; font-weight: 600; font-size: 22px;
  }
  .contact-phone {
    position: absolute; left: 0; width: 100%; top: 38px; display: flex; justify-content: center; align-items: center; gap: 6px;
    font-family: "Jost", sans-serif; font-weight: 500; font-size: 23px;
  }
  .contact-links { position: absolute; left: 34px; top: 40px; font-size: 11px; font-weight: 600; line-height: 18px; }
  .contact-links div, .contact-address { display: flex; align-items: center; gap: 9px; }
  .contact-address { position: absolute; left: 518px; top: 41px; font-size: 11px; font-weight: 600; line-height: 13px; align-items: flex-start; }
</style>
</head>
<body>
<div class="sheet">
  <svg class="hero" width="701" height="425" viewBox="0 0 701 425">
    <defs>
      <linearGradient id="heroTone" x1="0" y1="0" x2="1" y2="1">
        <stop offset="0" stop-color="#6f7c8c"/>
        <stop offset=".45" stop-color="#e9ecef"/>
        <stop offset=".8" stop-color="#b9bec4"/>
        <stop offset="1" stop-color="#3a3d44"/>
      </linearGradient>
    </defs>
    <polygon points="0,0 701,0 701,402 0,252" fill="url(#heroTone)" role="img" aria-label="Photo of a hand touching a tablet showing a rising bar chart among floating screens"/>
    <polygon points="0,252 701,402 701,410 0,288" fill="#0e5591"/>
    <polygon points="0,288 701,410 701,420 0,318" fill="#f07c22"/>
  </svg>

  <div class="brand">
    <span class="brand-square"></span>
    <span class="brand-name">Vantner &amp; Company</span>
  </div>

  <h1 class="title">Algorithmic Trading Strategy Overview</h1>
  <p class="intro">Vantner &amp; Company has partnered with an award winning algorithmic trading platform and developed a custom suite of algorithms designed to ensure high quality execution. Our algorithms incorporate our unique Northgate Exchange point of sale order types (sQuote* / pQuote*) seamlessly into each strategy. This integration smooth’s workflow, improves execution quality, ensures greater liquidity sourcing, minimizes information leakage and brings a wide variety of Algo and SOR strategies directly into your OMS, EMS, or proprietary trading platform. In addition, we work in a consultative role to develop custom DMA routes, design algorithms according to client needs or specific requirements, and implement unique routing strategies designed to efficiently touch today’s complex market micro-strategy.</p>

  <section class="strategies">
    <div class="column liquidity">
      <div class="tab">LIQUIDITY<br>SOURCING</div>
      <h2 class="strategy-name">SOR*</h2>
      <p class="strategy-text">Optimizes order placement in lit and dark venues to maximize liquidity capture and minimize information leakage. The strategy balances “Urgency to capture the display quote” vs. opportunities to seek out dark liquidity to minimize information leakage and price improvement.</p>
      <h2 class="strategy-name">DARK AGG</h2>
      <p class="strategy-text">Manages orderplacement in darkvenues to optimize liquidity capture and reduce information leakage. The strategy attempts to first discover liquidity by slicing optimally sized orders at various venues, and then rebalances intelligently to venues where it has detected liquidity.</p>
    </div>
    <div class="column schedule">
      <div class="tab">SCHEDULE<br>DRIVEN</div>
      <h2 class="strategy-name">VWAP*</h2>
      <p class="strategy-text">Trades using historical volume profile to target VWAP as the benchmark. The strategy can optionally accept StartTime and EndTime as parameters to schedule trading in a given trading period. The strategy utilizes passive and aggressive trading tactics to achieve liquidity.</p>
      <h2 class="strategy-name">TWAP*</h2>
      <p class="strategy-text">Similar to the VWAP strategy with a different schedule. The schedule is a constant rate of trading between the given StartTime and EndTime.</p>
    </div>
    <div class="column dynamic">
      <div class="tab">DYNAMIC &amp;<br>ADAPTIVE</div>
      <h2 class="strategy-name">POV*</h2>
      <p class="strategy-text">Tracks volume from the time the order starts trading and trades according to the specified target participation percentage. Continuous optimizations are made as the order trades to target optima price and liquidity goals.</p>
      <h2 class="strategy-name">ARRIVAL PRICE*</h2>
      <p class="strategy-text">Manages the trade-off between market impact and volatility (price risk) to optimally execute the order.</p>
      <p class="footnote">*Indicates sQuote/ pQuote</p>
    </div>
  </section>

  <div class="rule"></div>
  <footer class="contact">
    <div class="contact-links">
      <div><svg width="11" height="9" viewBox="0 0 11 9"><rect x=".5" y=".5" width="10" height="8" fill="#fff" stroke="#fff"/><polyline points="1,1 5.5,5 10,1" fill="none" stroke="#e0661a"/></svg>algosales@vantner.com</div>
      <div><svg width="11" height="11" viewBox="0 0 11 11"><circle cx="5.5" cy="5.5" r="5" fill="#fff"/><path d="M.5 5.5h10M5.5 .5c-2.5 3-2.5 7 0 10M5.5 .5c2.5 3 2.5 7 0 10" fill="none" stroke="#e0661a" stroke-width=".8"/></svg>www.Vantner.com</div>
    </div>
    <div class="contact-name">Contact: Dana Whitlock</div>
    <div class="contact-phone">
      <svg width="18" height="20" viewBox="0 0 18 20"><path d="M4 1l3 4-2 2c1 3 3 5 6 7l2-2 4 3-2 3C8 18 1 10 1 4z" fill="#fff"/></svg>
      646-555-0182
    </div>
    <div class="contact-address">
      <svg width="9" height="13" viewBox="0 0 9 13"><path d="M4.5 0a4.5 4.5 0 0 1 4.5 4.5C9 8 4.5 13 4.5 13S0 8 0 4.5A4.5 4.5 0 0 1 4.5 0z" fill="#fff"/><circle cx="4.5" cy="4.5" r="1.6" fill="#e0661a"/></svg>
      <span>48 Harbor Street, New York,<br>NY 10004</span>
    </div>
  </footer>
</div>
</body>
</html>
```